Orvin Studios First Business Card

I'm a real estate photographer in Maryland who also does 3D scans, walk through videos and use a drone for pictures and video as well. I have my drone license to fly commercially. I need a business card for my small business. I was thinking of just the dark logo on one side and contact/business info on the other but open to other creative ideas.
Target Market(s)
Real estate agents in Maryland
Industry/Entity Type
Real Estate
Contact Information for Business Card
Name: Derek Mallowby, Position: Photographer and Owner, Email: derek@orvinstudios.example, Website: orvinstudios.example, Phone: 301-867-3915
Look and feel
Each slider illustrates characteristics of the customer's brand and the style your logo design should communicate.

```html
<!DOCTYPE html>
<html lang="en">
<head>
<meta charset="utf-8">
<title>Orvin Studios – Business Card</title>
<link href="https://fonts.googleapis.com/css2?family=Montserrat:wght@300;400;700&display=swap" rel="stylesheet">
<style>
  :root {
    --backdrop: #6a6a69;
    --card: #171717;
    --accent: #e9c6a8;
    --ink-light: #f4f1ee;
    --card-w: 540px;
    --card-h: 309px;
  }
  * { box-sizing: border-box; margin: 0; padding: 0; }
  html, body {
    width: 1200px;
    height: 801px;
    overflow: hidden;
    background: var(--backdrop);
    font-family: "Montserrat", sans-serif;
  }
  .sheet {
    position: relative;
    width: 1200px;
    height: 801px;
    display: flex;
    align-items: center;
    justify-content: center;
    gap: 40px;
  }
  .card {
    width: var(--card-w);
    height: var(--card-h);
    background: var(--card);
    position: relative;
    border-bottom: 2px solid var(--accent);
  }

  /* Front: contact side */
  .card-front {
    display: flex;
    align-items: center;
    justify-content: center;
    gap: 26px;
  }
  .identity {
    text-align: right;
  }
  .identity-name {
    color: var(--accent);
    font-weight: 700;
    font-size: 25px;
    letter-spacing: 0.2px;
    line-height: 1.1;
  }
  .identity-role {
    color: var(--ink-light);
    font-weight: 300;
    font-size: 15px;
    margin-top: 4px;
  }
  .divider {
    width: 1px;
    height: 62px;
    background: var(--accent);
  }
  .contact-list {
    list-style: none;
    display: flex;
    flex-direction: column;
    gap: 7px;
  }
  .contact-item {
    display: flex;
    align-items: center;
    gap: 9px;
    color: var(--ink-light);
    font-weight: 300;
    font-size: 14px;
  }
  .contact-icon {
    width: 13px;
    height: 13px;
    flex: none;
  }

  /* Back: brand side */
  .card-back {
    display: flex;
    align-items: center;
    justify-content: center;
  }
  .brand-name {
    color: var(--accent);
    font-weight: 300;
    font-size: 46px;
    letter-spacing: 2px;
    text-transform: uppercase;
  }
</style>
</head>
<body>
<main class="sheet">
  <section class="card card-front" aria-label="Business card, contact side">
    <div class="identity">
      <p class="identity-name">Derek Mallowby</p>
      <p class="identity-role">Photographer and Owner</p>
    </div>
    <span class="divider" aria-hidden="true"></span>
    <ul class="contact-list">
      <li class="contact-item">
        <svg class="contact-icon" viewBox="0 0 16 16" aria-hidden="true">
          <path fill="var(--accent)" d="M3.6 1.2l2.3 2.6-1.4 1.8c.9 2 2.9 4 4.9 4.9l1.8-1.4 2.6 2.3-1.2 2.1C7.4 15.1.9 8.6 1.5 2.4z"/>
        </svg>
        <span>301-867-3915</span>
      </li>
      <li class="contact-item">
        <svg class="contact-icon" viewBox="0 0 16 16" aria-hidden="true">
          <rect x="1" y="3" width="14" height="10" fill="var(--accent)"/>
          <path d="M1.5 3.5L8 9l6.5-5.5" fill="none" stroke="var(--card)" stroke-width="1.2"/>
        </svg>
        <span>derek@orvinstudios.example</span>
      </li>
      <li class="contact-item">
        <svg class="contact-icon" viewBox="0 0 16 16" aria-hidden="true">
          <circle cx="8" cy="8" r="6.5" fill="none" stroke="var(--accent)" stroke-width="1.3"/>
          <ellipse cx="8" cy="8" rx="2.8" ry="6.5" fill="none" stroke="var(--accent)" stroke-width="1.1"/>
          <path d="M1.5 8h13" stroke="var(--accent)" stroke-width="1.1"/>
        </svg>
        <span>orvinstudios.example</span>
      </li>
    </ul>
  </section>

  <section class="card card-back" aria-label="Business card, brand side">
    <p class="brand-name">Orvin Studios</p>
  </section>
</main>
</body>
</html>
```